Design required for boutique fire engineering firm in New Zealand

Our website was published based on free Wordpress templates, we'd like something a bit more bespoke, clean and simple.

Reason: didn't check this finished on a Sunday :)

Target Market(s)

architects, building owners, property developers

Industry/Entity Type

Boutique

Contact Information for Business Card

Logo
Fire Engineering

Derek Holloway
Principal
+64 21 738 152
derek@veltraxa.nz
veltraxa.nz

Number of Pages Required

3 page

Font styles to use
Sans Serif

Requirements
Nice to have
• On the business card, an embossed logo would be great - not sure if that's a design thing or just a print thing?
• Website, existing @ http://veltraxa.nz for extent of content and general arrangement that I'm happy with.
• Ability to update the content with project bio's and some photos at a later date would be nice.

```html
<!DOCTYPE html>
<html lang="en">
<head>
<meta charset="utf-8">
<title>Veltraxa — Consulting Fire Engineers</title>
<link href="https://fonts.googleapis.com/css2?family=Poppins:wght@400;500;600&family=Open+Sans:wght@400;600&display=swap" rel="stylesheet">
<style>
:root{
  --navy:#1d4e7e;
  --blue:#2f6fae;
  --band:#1c5a8a;
  --ink:#333a44;
  --muted:#555d68;
  --light:#f3f4f6;
  --footer:#16191d;
  --white:#ffffff;
}
*{margin:0;padding:0;box-sizing:border-box}
html,body{width:1200px;height:2908px;overflow:hidden}
body{font-family:"Open Sans",Arial,sans-serif;color:var(--ink);background:var(--white);position:relative}
h1,h2,h3,h4,.brand,.nav a,.btn{font-family:"Poppins",Arial,sans-serif}
section,header,footer{position:absolute;left:0;width:1200px}
.abs{position:absolute}

/* header */
.site-header{top:0;height:91px;background:var(--white)}
.brand{left:100px;top:22px;display:flex;align-items:center;gap:10px;font-size:38px;font-weight:600;color:var(--navy);line-height:46px}
.brand-dot{width:46px;height:46px;border-radius:50%;background:var(--navy)}
.nav{right:96px;top:34px;display:flex;gap:28px;font-size:17px;align-items:center}
.nav a{color:#222;text-decoration:none}

/* hero */
.hero{top:91px;height:533px;background:linear-gradient(180deg,#1a2230 0%,#2a3140 45%,#3a3d48 62%,#1c2230 80%,#141924 100%)}
.hero-ring{left:550px;top:180px;width:100px;height:100px;border:4px solid var(--white);border-radius:50%}
.hero h1{left:0;width:1200px;top:290px;text-align:center;color:var(--white);font-size:31px;font-weight:600;line-height:40px}
.hero-dots{left:566px;top:485px;display:flex;gap:4px}
.hero-dots span{width:14px;height:14px;border:2px solid var(--white);border-radius:50%}

/* about */
.about{top:624px;height:477px}
.about h2{left:100px;top:85px;font-size:37px;font-weight:500;color:var(--navy)}
.about p{left:100px;width:570px;font-size:12.5px;line-height:22px;color:var(--muted)}
.btn{display:inline-block;background:var(--blue);color:var(--white);font-size:12px;font-weight:500;padding:8px 14px;border-radius:3px;text-transform:uppercase}
.about-frame{left:742px;top:145px;width:200px;height:200px;border:2px solid #d7d9dc;transform:rotate(45deg)}
.about-photo{left:680px;top:40px;width:340px;height:437px;background:linear-gradient(180deg,#e9d98a 0%,#9fc3de 35%,#7ea6c8 70%,#8b6a4d 100%);border-radius:160px 160px 0 0}

/* services */
.services{top:1101px;height:510px;background:linear-gradient(135deg,#1f5e90,#17507f)}
.services h2{left:0;width:1200px;top:68px;text-align:center;color:var(--white);font-size:30px;font-weight:500}
.service{top:170px;width:240px;text-align:center;color:var(--white)}
.service svg{display:block;margin:0 auto}
.service h3{font-size:18px;font-weight:500;margin-top:14px}
.service p{font-size:12px;line-height:20px;margin-top:8px;opacity:.92}
.service .chev{margin-top:12px}

/* consulting */
.consulting{top:1611px;height:524px}
.video-shadow{left:118px;top:98px;width:466px;height:312px;background:#e8e9eb}
.video{left:110px;top:108px;width:466px;height:312px;background:linear-gradient(160deg,#c9d6e4 0%,#b8a27a 45%,#6d6458 100%)}
.play{left:306px;top:236px;width:60px;height:60px;border:3px solid var(--white);border-radius:50%}
.consulting h2{left:630px;top:90px;font-size:37px;font-weight:500;color:var(--navy)}
.consulting p{left:630px;top:155px;width:470px;font-size:12.5px;line-height:24px;color:var(--muted)}
.ticks{left:630px;top:258px;list-style:none;font-size:12.5px;color:var(--muted)}
.ticks li{display:flex;align-items:center;gap:12px;height:30px}

/* news */
.news{top:2135px;height:372px;background:var(--light)}
.news h2{left:100px;top:52px;font-size:29px;font-weight:600;color:var(--navy)}
.arrows{left:1058px;top:62px;font-size:14px;color:#333;letter-spacing:12px}
.card-img{top:136px;width:188px;height:162px;background:linear-gradient(180deg,#e6e2d8,#c4a890 60%,#8aa2b8)}
.card h3{font-size:16px;line-height:22px;font-weight:400;color:var(--blue);width:260px}
.card .date{font-size:12px;font-weight:600;margin-top:18px}
.card .txt{font-size:11.5px;line-height:19px;color:var(--muted);margin-top:10px;width:265px}
.card .more{font-size:12px;margin-top:14px}

/* footer */
.site-footer{top:2507px;height:310px;background:linear-gradient(180deg,#121518,#1d2126);color:var(--white)}
.site-footer h4{font-size:17px;font-weight:600;text-transform:uppercase}
.site-footer .col{top:50px}
.small{font-size:11.5px;line-height:19px}
.email-field{width:305px;height:40px;background:var(--white);color:#666;font-size:11px;padding:12px 14px;margin-top:20px}
.sub{margin-top:10px;background:var(--blue);width:132px;height:40px;line-height:40px;text-align:center;font-size:14px;font-family:"Poppins",Arial,sans-serif}
.contact-row{display:flex;gap:16px;align-items:center;font-size:12.5px;margin-top:14px}
.links{list-style:none;font-size:12px;margin-top:18px}
.links li{height:26px}
.links li::before{content:"›";margin-right:12px}
.social{list-style:none;font-size:13.5px;margin-top:16px}
.social li{display:flex;align-items:center;gap:10px;height:37px}
.social span.c{width:26px;height:26px;border:1.5px solid var(--white);border-radius:50%}
.bottom-bar{top:2817px;height:91px;background:var(--blue);color:var(--white)}
.bottom-dot{left:572px;top:-22px;width:56px;height:56px;border-radius:50%;background:var(--navy);border:4px solid var(--white)}
.bottom-bar p{left:0;width:1200px;top:54px;text-align:center;font-size:11.5px}
</style>
</head>
<body>

<header class="site-header">
  <div class="brand abs"><span class="brand-dot"></span>veltraxa</div>
  <nav class="nav abs">
    <a href="#">Home</a><a href="#">About Us</a><a href="#">Consulting Services</a><a href="#">News</a><a href="#">Contact Us</a>
    <svg width="18" height="18" viewBox="0 0 18 18" aria-label="Search"><circle cx="7.5" cy="7.5" r="5.5" fill="none" stroke="#222" stroke-width="2.4"/><line x1="11.5" y1="11.5" x2="16" y2="16" stroke="#222" stroke-width="2.6"/></svg>
  </nav>
</header>

<section class="hero" role="img" aria-label="Night city skyline with lit towers reflected on a harbour">
  <div class="hero-ring abs"></div>
  <h1 class="abs">Consulting fire engineers based<br>in Wellington, New Zealand</h1>
  <div class="hero-dots abs"><span></span><span></span><span></span><span></span></div>
</section>

<section class="about">
  <h2 class="abs">About Veltraxa</h2>
  <p class="abs" style="top:148px">Veltraxa is a boutique fire engineering firm based in Wellington, New Zealand, founded by Derek Holloway in 2017. We provide consulting services in the built environment, including design and review services to assist in Building Consent applications, advice on property protection matters, observation of construction on site, and regulatory consultation.</p>
  <p class="abs" style="top:258px">Derek has worked as a fire engineer in New Zealand for over 20 years, having graduated from the University of Harrowgate with a Bachelors of Engineering (with Honours) and Masters of Engineering in Fire Engineering, and is a Chartered Professional Engineer.</p>
  <span class="btn abs" style="left:100px;top:354px">Read more ⊕</span>
  <div class="about-frame abs"></div>
  <div class="about-photo abs" role="img" aria-label="Engineer in a yellow hard hat and checked shirt holding a clipboard"></div>
</section>

<section class="services">
  <h2 class="abs">OUR SERVICES</h2>
  <div class="service abs" style="left:86px">
    <svg width="122" height="122" viewBox="0 0 122 122"><circle cx="61" cy="61" r="54" fill="none" stroke="#fff" stroke-width="8" stroke-dasharray="0 7 155.65 7"/><circle cx="56" cy="64" r="11" fill="none" stroke="#fff" stroke-width="7" stroke-dasharray="4 3"/><circle cx="56" cy="64" r="3" fill="#fff"/><circle cx="72" cy="49" r="6" fill="none" stroke="#fff" stroke-width="4" stroke-dasharray="3 2"/></svg>
    <h3>Built Environment</h3>
    <p>Nemo enim ipsam voluptatem quia volut sit aspernatur aut odit aut fugit, sed quia consequuntur magni dolores</p>
    <svg class="chev" width="18" height="18" viewBox="0 0 18 18"><path d="M3 3l6 5 6-5M3 9l6 5 6-5" fill="none" stroke="#fff" stroke-width="2"/></svg>
  </div>
  <div class="service abs" style="left:350px">
    <svg width="122" height="122" viewBox="0 0 122 122"><circle cx="61" cy="61" r="54" fill="none" stroke="#fff" stroke-width="8" stroke-dasharray="0 7 155.65 7"/><rect x="46" y="40" width="26" height="38" fill="#fff"/><path d="M51 50h16M51 57h16M51 64h10" stroke="var(--band)" stroke-width="2.4"/><path d="M68 74l11-15 5 3-11 15z" fill="#fff" stroke="var(--band)" stroke-width="1.5"/></svg>
    <h3>Building Consent</h3>
    <p>Nemo enim ipsam voluptatem quia volut sit aspernatur aut odit aut fugit, sed quia consequuntur magni dolores</p>
    <svg class="chev" width="18" height="18" viewBox="0 0 18 18"><path d="M3 3l6 5 6-5M3 9l6 5 6-5" fill="none" stroke="#fff" stroke-width="2"/></svg>
  </div>
  <div class="service abs" style="left:614px">
    <svg width="122" height="122" viewBox="0 0 122 122"><circle cx="61" cy="61" r="54" fill="none" stroke="#fff" stroke-width="8" stroke-dasharray="0 7 155.65 7"/><path d="M38 62l23-21 23 21h-6v17H44V62z" fill="#fff"/><rect x="56" y="66" width="10" height="13" fill="var(--band)"/></svg>
    <h3>Property Protection</h3>
    <p>Nemo enim ipsam voluptatem quia volut sit aspernatur aut odit aut fugit, sed quia consequuntur magni dolores</p>
    <svg class="chev" width="18" height="18" viewBox="0 0 18 18"><path d="M3 3l6 5 6-5M3 9l6 5 6-5" fill="none" stroke="#fff" stroke-width="2"/></svg>
  </div>
  <div class="service abs" style="left:874px">
    <svg width="122" height="122" viewBox="0 0 122 122"><circle cx="61" cy="61" r="54" fill="none" stroke="#fff" stroke-width="8" stroke-dasharray="0 7 155.65 7"/><circle cx="61" cy="51" r="11" fill="#fff"/><path d="M41 80a20 17 0 0 1 40 0z" fill="#fff"/></svg>
    <h3>Regulatory Consultation</h3>
    <p>Nemo enim ipsam voluptatem quia volut sit aspernatur aut odit aut fugit, sed quia consequuntur magni dolores</p>
    <svg class="chev" width="18" height="18" viewBox="0 0 18 18"><path d="M3 3l6 5 6-5M3 9l6 5 6-5" fill="none" stroke="#fff" stroke-width="2"/></svg>
  </div>
</section>

<section class="consulting">
  <div class="video-shadow abs"></div>
  <div class="video abs" role="img" aria-label="Engineers in hard hats reviewing plans on a rooftop site"></div>
  <div class="play abs"><svg width="54" height="54" viewBox="0 0 54 54"><path d="M21 16l17 11-17 11z" fill="#fff"/></svg></div>
  <h2 class="abs">Consulting Fire Engineers</h2>
  <p class="abs">Lorem ipsum dolor sit amet, consectetur adipiscing elit, sed do eiusmod tempor ididunt ut labore et dolore magna aliqua. Ut enim ad minim veniam, quis nostrud exercitation ullamco laboris nisi ut aliquip ex ea commodo consequat. Duis aute irure dolor in reprehenderit in voluptate velit esse cillum dolore</p>
  <ul class="ticks abs">
    <li><svg width="12" height="10" viewBox="0 0 12 10"><path d="M1 5l3.5 3.5L11 1" fill="none" stroke="var(--navy)" stroke-width="2.4"/></svg>Nam suscipit leo at gravida aliquam.</li>
    <li><svg width="12" height="10" viewBox="0 0 12 10"><path d="M1 5l3.5 3.5L11 1" fill="none" stroke="var(--navy)" stroke-width="2.4"/></svg>Praesent eget augue mollis, hendrerit mauris eget, dignissim nisi.</li>
    <li><svg width="12" height="10" viewBox="0 0 12 10"><path d="M1 5l3.5 3.5L11 1" fill="none" stroke="var(--navy)" stroke-width="2.4"/></svg>Proin ac eros tempor, dictum ex eget, fermentum nibh.</li>
  </ul>
  <span class="btn abs" style="left:630px;top:370px;font-size:13px;padding:9px 18px">Read more</span>
</section>

<section class="news">
  <h2 class="abs">LATEST NEWS</h2>
  <div class="arrows abs">← →</div>
  <div class="card-img abs" style="left:100px" role="img" aria-label="Child in a white hard hat holding a model house"></div>
  <div class="card abs" style="left:312px;top:132px">
    <h3>Sed ut perspiciatis unde omnis natus error sit voluptatem</h3>
    <div class="date">MAY 25, 2017</div>
    <div class="txt">Nemo enim ipsam voluptatem quia voluptas sit aspernatur aut odit aut fugit, sed quia consequuntur magni dolores eos qui ratione</div>
    <div class="more">Read More +</div>
  </div>
  <div class="card-img abs" style="left:642px" role="img" aria-label="Team in yellow hard hats studying drawings"></div>
  <div class="card abs" style="left:853px;top:132px">
    <h3>Sed ut perspiciatis unde omnis natus error sit voluptatem</h3>
    <div class="date">MAY 25, 2017</div>
    <div class="txt">Nemo enim ipsam voluptatem quia voluptas sit aspernatur aut odit aut fugit, sed quia consequuntur magni dolores eos qui ratione</div>
    <div class="more">Read More +</div>
  </div>
</section>

<footer class="site-footer">
  <div class="col abs" style="left:100px">
    <h4>Join our newsletter</h4>
    <p class="small" style="margin-top:16px;width:260px">Sed ut perspiciatis unde omnis iste natus error sit voluptatem accusantium dolore</p>
    <div class="email-field">Enter Email</div>
    <div class="sub">SUBSCRIBE</div>
  </div>
  <div class="col abs" style="left:500px">
    <h4>Contact us</h4>
    <p class="small" style="margin-top:18px">Veltraxa<br>418 Harbourline Terrace<br>Kelburn, New Zealand</p>
    <div class="contact-row" style="margin-top:18px"><svg width="20" height="20" viewBox="0 0 20 20"><path d="M4 2l4 1 1 4-2 2a11 11 0 0 0 4 4l2-2 4 1 1 4-3 2C8 17 3 12 2 5z" fill="none" stroke="#fff" stroke-width="1.4"/></svg>Phone: 04-732-1185</div>
    <div class="contact-row" style="margin-top:20px"><svg width="20" height="16" viewBox="0 0 20 16"><rect x="1" y="2" width="18" height="12" fill="none" stroke="#fff" stroke-width="1.4"/><path d="M1 2l9 7 9-7" fill="none" stroke="#fff" stroke-width="1.4"/></svg>Email: info@veltraxa.nz</div>
  </div>
  <div class="col abs" style="left:800px">
    <h4>Quick links</h4>
    <ul class="links"><li>Home</li><li>About Us</li><li>Our Services</li><li>Blog</li><li>Contact Us</li></ul>
  </div>
  <div class="col abs" style="left:1004px">
    <h4>Social</h4>
    <ul class="social"><li><span class="c"></span>Newsfeed</li><li><span class="c"></span>Updates</li><li><span class="c"></span>Circles</li><li><span class="c"></span>Videos</li></ul>
  </div>
</footer>

<div class="bottom-bar abs" style="left:0;width:1200px">
  <div class="bottom-dot abs"></div>
  <p class="abs">Copyright 2017 | All Rights Reserved – Veltraxa</p>
</div>

</body>
</html>
```